Breakfast Briefings / Lunch & Learn

I would like to have a double sided flyer size 8x10 to display the breakfast briefing on one side and Lunch & Learn on the other side.

Header on each side to say
2018 Calendar Breakfast Briefing (on the breakfast side)
2018 Calendar Lunch & Learn (on the lunch side)

I have attached a copy of the files we would like to use.

Learn

```html
<!DOCTYPE html>
<html lang="en">
<head>
<meta charset="utf-8">
<title>Lunch &amp; Learn 2018 Calendar</title>
<link rel="stylesheet" href="https://fonts.googleapis.com/css2?family=Audiowide&family=Carlito:ital,wght@0,400;0,700;1,700&display=swap">
<style>
  :root {
    --orange: #e8771e;
    --orange-light: #f08a2c;
    --teal: #179a8a;
    --teal-line: #3fb3a4;
    --magenta: #e0197a;
    --magenta-deep: #c0126a;
    --green: #8cc63f;
    --green-light: #a2d25a;
    --white: #ffffff;
    --ink: #111111;
    --display: "Audiowide", sans-serif;
    --body: "Carlito", sans-serif;
  }
  * { box-sizing: border-box; margin: 0; padding: 0; }
  html, body { width: 1008px; height: 1200px; overflow: hidden; background: var(--white); }
  .flyer { position: relative; width: 1008px; height: 1200px; background: var(--white); }

  .title-bar {
    position: absolute; left: 0; top: 0; width: 1008px; height: 56px;
    background: var(--orange); color: var(--white);
    font-family: var(--display); font-size: 36px; text-align: center; line-height: 58px;
  }

  .schedule {
    position: absolute; left: 251px; top: 71px; width: 376px; height: 590px;
    background: var(--teal); padding: 24px 24px 0 24px;
    font-family: var(--body); color: var(--ink);
  }
  .session { height: 50px; }
  .session-month { font-weight: 700; font-size: 20px; line-height: 22px; }
  .session-topic {
    font-size: 17px; line-height: 24px; padding-left: 2px;
    border: 1px solid var(--teal-line); border-left: none; border-right: none;
  }
  .schedule-blank { height: 30px; border: 1px solid var(--teal-line); border-left: none; border-right: none; margin-top: 4px; }

  .motto-tile {
    position: absolute; left: 635px; top: 71px; width: 124px; height: 210px;
    background: radial-gradient(circle at 50% 40%, var(--orange-light), var(--orange));
  }
  .motto {
    position: absolute; left: 0; right: 4px; bottom: 6px; text-align: right;
    font-family: var(--body); font-style: italic; font-weight: 700; font-size: 15px; color: var(--white);
  }

  .utensil-tile {
    position: absolute; left: 635px; top: 295px; width: 124px; height: 447px;
    background: linear-gradient(180deg, var(--magenta), var(--magenta-deep) 140%);
  }

  .sponsor-band {
    position: absolute; left: 251px; top: 673px; width: 376px; height: 69px;
    background: radial-gradient(circle at 50% 50%, var(--green-light), var(--green));
    display: flex; align-items: center; justify-content: center;
  }
  .sponsor-name {
    color: var(--white);
    font-family: var(--body); font-weight: 700; font-size: 18px;
  }

  .calendar {
    position: absolute; left: 0; top: 757px; width: 1008px; height: 443px;
    background: var(--orange); color: var(--white); font-family: var(--display);
  }
  .calendar-year { position: absolute; right: 22px; top: 2px; font-size: 44px; line-height: 50px; }
  .month { position: absolute; width: 214px; }
  .month-name { font-size: 17px; line-height: 20px; margin-bottom: 1px; }
  .days { display: grid; grid-template-columns: repeat(7, 30px); font-size: 11px; line-height: 14px; }
  .days span { text-align: left; padding-left: 4px; }

  .c1 { left: 17px; } .c2 { left: 269px; } .c3 { left: 523px; } .c4 { left: 776px; }
  .r1 { top: 51px; } .r2 { top: 186px; } .r3 { top: 320px; }
  .s1 { grid-column-start: 1; } .s2 { grid-column-start: 2; } .s3 { grid-column-start: 3; }
  .s4 { grid-column-start: 4; } .s5 { grid-column-start: 5; } .s6 { grid-column-start: 6; } .s7 { grid-column-start: 7; }
</style>
</head>
<body>
<main class="flyer">
  <header class="title-bar">Lunch &amp; Learn</header>

  <section class="schedule">
    <div class="session"><div class="session-month">March:</div><div class="session-topic">Mindfulness</div></div>
    <div class="session"><div class="session-month">April:</div><div class="session-topic">Nutrition and Lifestyle Coaching</div></div>
    <div class="session"><div class="session-month">May:</div><div class="session-topic">What is Neuromodulation?</div></div>
    <div class="session"><div class="session-month">June:</div><div class="session-topic">Achieve Your Goals</div></div>
    <div class="session"><div class="session-month">July:</div><div class="session-topic">Changing Your Life Positive Thinking</div></div>
    <div class="session"><div class="session-month">August:</div><div class="session-topic">Clean Eating How Do I Get Started</div></div>
    <div class="session"><div class="session-month">September:</div><div class="session-topic">Budgeting 101 Financial Wellness</div></div>
    <div class="session"><div class="session-month">October:</div><div class="session-topic">Busted! Nutrition Myths</div></div>
    <div class="session"><div class="session-month">November:</div><div class="session-topic">Time Management</div></div>
    <div class="session"><div class="session-month">December:</div><div class="session-topic">First Time Home Buyers</div></div>
    <div class="schedule-blank"></div>
  </section>

  <div class="motto-tile" role="img" aria-label="Orange swirl pattern tile">
    <span class="motto">Life. Long. Learn</span>
  </div>

  <div class="utensil-tile" role="img" aria-label="Illustration of a pencil, an ampersand and a fork in black on magenta"></div>

  <div class="sponsor-band" role="img" aria-label="Green swirl pattern band with sponsor name">
    <span class="sponsor-name">Tellmarsh</span>
  </div>

  <section class="calendar">
    <div class="calendar-year">2018</div>

    <div class="month c1 r1"><div class="month-name">January</div><div class="days">
      <span>M</span><span>T</span><span>W</span><span>T</span><span>F</span><span>S</span><span>S</span>
      <span class="s1">1</span><span>2</span><span>3</span><span>4</span><span>5</span><span>6</span><span>7</span><span>8</span><span>9</span><span>10</span><span>11</span><span>12</span><span>13</span><span>14</span><span>15</span><span>16</span><span>17</span><span>18</span><span>19</span><span>20</span><span>21</span><span>22</span><span>23</span><span>24</span><span>25</span><span>26</span><span>27</span><span>28</span><span>29</span><span>30</span><span>31</span>
    </div></div>

    <div class="month c2 r1"><div class="month-name">February</div><div class="days">
      <span>M</span><span>T</span><span>W</span><span>T</span><span>F</span><span>S</span><span>S</span>
      <span class="s4">1</span><span>2</span><span>3</span><span>4</span><span>5</span><span>6</span><span>7</span><span>8</span><span>9</span><span>10</span><span>11</span><span>12</span><span>13</span><span>14</span><span>15</span><span>16</span><span>17</span><span>18</span><span>19</span><span>20</span><span>21</span><span>22</span><span>23</span><span>24</span><span>25</span><span>26</span><span>27</span><span>28</span>
    </div></div>

    <div class="month c3 r1"><div class="month-name">March</div><div class="days">
      <span>M</span><span>T</span><span>W</span><span>T</span><span>F</span><span>S</span><span>S</span>
      <span class="s4">1</span><span>2</span><span>3</span><span>4</span><span>5</span><span>6</span><span>7</span><span>8</span><span>9</span><span>10</span><span>11</span><span>12</span><span>13</span><span>14</span><span>15</span><span>16</span><span>17</span><span>18</span><span>19</span><span>20</span><span>21</span><span>22</span><span>23</span><span>24</span><span>25</span><span>26</span><span>27</span><span>28</span><span>29</span><span>30</span><span>31</span>
    </div></div>

    <div class="month c4 r1"><div class="month-name">April</div><div class="days">
      <span>M</span><span>T</span><span>W</span><span>T</span><span>F</span><span>S</span><span>S</span>
      <span class="s7">1</span><span>2</span><span>3</span><span>4</span><span>5</span><span>6</span><span>7</span><span>8</span><span>9</span><span>10</span><span>11</span><span>12</span><span>13</span><span>14</span><span>15</span><span>16</span><span>17</span><span>18</span><span>19</span><span>20</span><span>21</span><span>22</span><span>23</span><span>24</span><span>25</span><span>26</span><span>27</span><span>28</span><span>29</span><span>30</span>
    </div></div>

    <div class="month c1 r2"><div class="month-name">May</div><div class="days">
      <span>M</span><span>T</span><span>W</span><span>T</span><span>F</span><span>S</span><span>S</span>
      <span class="s2">1</span><span>2</span><span>3</span><span>4</span><span>5</span><span>6</span><span>7</span><span>8</span><span>9</span><span>10</span><span>11</span><span>12</span><span>13</span><span>14</span><span>15</span><span>16</span><span>17</span><span>18</span><span>19</span><span>20</span><span>21</span><span>22</span><span>23</span><span>24</span><span>25</span><span>26</span><span>27</span><span>28</span><span>29</span><span>30</span><span>31</span>
    </div></div>

    <div class="month c2 r2"><div class="month-name">June</div><div class="days">
      <span>M</span><span>T</span><span>W</span><span>T</span><span>F</span><span>S</span><span>S</span>
      <span class="s5">1</span><span>2</span><span>3</span><span>4</span><span>5</span><span>6</span><span>7</span><span>8</span><span>9</span><span>10</span><span>11</span><span>12</span><span>13</span><span>14</span><span>15</span><span>16</span><span>17</span><span>18</span><span>19</span><span>20</span><span>21</span><span>22</span><span>23</span><span>24</span><span>25</span><span>26</span><span>27</span><span>28</span><span>29</span><span>30</span>
    </div></div>

    <div class="month c3 r2"><div class="month-name">July</div><div class="days">
      <span>M</span><span>T</span><span>W</span><span>T</span><span>F</span><span>S</span><span>S</span>
      <span class="s7">1</span><span>2</span><span>3</span><span>4</span><span>5</span><span>6</span><span>7</span><span>8</span><span>9</span><span>10</span><span>11</span><span>12</span><span>13</span><span>14</span><span>15</span><span>16</span><span>17</span><span>18</span><span>19</span><span>20</span><span>21</span><span>22</span><span>23</span><span>24</span><span>25</span><span>26</span><span>27</span><span>28</span><span>29</span><span>30</span><span>31</span>
    </div></div>

    <div class="month c4 r2"><div class="month-name">August</div><div class="days">
      <span>M</span><span>T</span><span>W</span><span>T</span><span>F</span><span>S</span><span>S</span>
      <span class="s3">1</span><span>2</span><span>3</span><span>4</span><span>5</span><span>6</span><span>7</span><span>8</span><span>9</span><span>10</span><span>11</span><span>12</span><span>13</span><span>14</span><span>15</span><span>16</span><span>17</span><span>18</span><span>19</span><span>20</span><span>21</span><span>22</span><span>23</span><span>24</span><span>25</span><span>26</span><span>27</span><span>28</span><span>29</span><span>30</span><span>31</span>
    </div></div>

    <div class="month c1 r3"><div class="month-name">September</div><div class="days">
      <span>M</span><span>T</span><span>W</span><span>T</span><span>F</span><span>S</span><span>S</span>
      <span class="s6">1</span><span>2</span><span>3</span><span>4</span><span>5</span><span>6</span><span>7</span><span>8</span><span>9</span><span>10</span><span>11</span><span>12</span><span>13</span><span>14</span><span>15</span><span>16</span><span>17</span><span>18</span><span>19</span><span>20</span><span>21</span><span>22</span><span>23</span><span>24</span><span>25</span><span>26</span><span>27</span><span>28</span><span>29</span><span>30</span>
    </div></div>

    <div class="month c2 r3"><div class="month-name">October</div><div class="days">
      <span>M</span><span>T</span><span>W</span><span>T</span><span>F</span><span>S</span><span>S</span>
      <span class="s1">1</span><span>2</span><span>3</span><span>4</span><span>5</span><span>6</span><span>7</span><span>8</span><span>9</span><span>10</span><span>11</span><span>12</span><span>13</span><span>14</span><span>15</span><span>16</span><span>17</span><span>18</span><span>19</span><span>20</span><span>21</span><span>22</span><span>23</span><span>24</span><span>25</span><span>26</span><span>27</span><span>28</span><span>29</span><span>30</span><span>31</span>
    </div></div>

    <div class="month c3 r3"><div class="month-name">November</div><div class="days">
      <span>M</span><span>T</span><span>W</span><span>T</span><span>F</span><span>S</span><span>S</span>
      <span class="s4">1</span><span>2</span><span>3</span><span>4</span><span>5</span><span>6</span><span>7</span><span>8</span><span>9</span><span>10</span><span>11</span><span>12</span><span>13</span><span>14</span><span>15</span><span>16</span><span>17</span><span>18</span><span>19</span><span>20</span><span>21</span><span>22</span><span>23</span><span>24</span><span>25</span><span>26</span><span>27</span><span>28</span><span>29</span><span>30</span>
    </div></div>

    <div class="month c4 r3"><div class="month-name">December</div><div class="days">
      <span>M</span><span>T</span><span>W</span><span>T</span><span>F</span><span>S</span><span>S</span>
      <span class="s6">1</span><span>2</span><span>3</span><span>4</span><span>5</span><span>6</span><span>7</span><span>8</span><span>9</span><span>10</span><span>11</span><span>12</span><span>13</span><span>14</span><span>15</span><span>16</span><span>17</span><span>18</span><span>19</span><span>20</span><span>21</span><span>22</span><span>23</span><span>24</span><span>25</span><span>26</span><span>27</span><span>28</span><span>29</span><span>30</span><span>31</span>
    </div></div>
  </section>
</main>
</body>
</html>
```